●お仕事の概要● インターネット上で通販印刷「カミエル。」を運営している「株式会社ルモンテック」と申します。 カミエル。 http://www.kamieru-example.jp/ 今回の依頼は、名刺印刷「カミエル。」(http://www.kamieru-example.jp/)で使用する【ハンドメイド台紙のデザイン】 を募集いたします。 募集したデザインは弊社サイトカミエル。「デザインを選んで名刺を作成」の「ハンドメイド台紙」として使用します。 https://kamieru-example.jp/design-order/ *古くからのデザインを掲載しておりますので、スタイリッシュで様々なシーンに使用できるデザインに 一新したいと考えております。 デザインの参考イメージは添付ファイル内「reference」フォルダ内に入れております。 ハンドメイド台紙とは、ハンドメイド用品(主にアクセサリー等)を売る時につける台紙です。 *「参考画像1」をご確認ください。 提案をお願いしたいデザインは4種類です。どのデザインで提案いただきましても問題ありません。 *「参考画像2」をご確認ください。 *背景が色ベタになっているイメージ画像ありますが、ベタ面は印刷時にムラが発生しやすいため 少ない方が好ましいです。 また今回も*複数採用*の募集となります。 契約成立の金額は下記金額となります。 上位 1位 5,000円(1点) 2位 3,000円(1点) その他 採用デザイン 1点:1,000円 (合計 20点ほどを予定しております。) 全応募デザインより弊社スタッフにてランク付けさせて頂き、上位1位の方には5千円、以下3,000円〜1,000円迄の報酬となります。 ※クオリティーなどにより20件未満の契約となる場合がございます ※逆によいデザインが沢山ある場合は20件以上採用いたします ●作成デザイン詳細● ※デザイン作成のときはテンプレート(添付ファイル)の使用をお願いします 1.ファイル形式 「ai」または「psd」形式 2.作成サイズ 名刺サイズ(91mm×55mmに上下左右3mmの塗り足し、つまり97mm×61mm) ※縦横どちらでも構いません ※psdファイルの場合は解像度350dpi、RGB形式でお願いします ※デザイン作成のときはテンプレート(添付ファイル)の使用をお願いします 3.作成デザインについて 【ハンドメイド台紙】を募集いたします。 今回仮で入れていただく内容は、お客様によって入力内容が異なりますので、入力内容に左右されないデザインを意識して作成お願いします。 *色ベタは印刷時にムラが発生しやすいため少ない方が好ましいです。 *グラデーションは印刷のムラが出やすいので、大きい面での使用を控えていただきたいです。 *枠がついているデザインは、断裁がズレた場合目立ちますので、枠なしの方が好ましいです。 4.お客様が編集する下記文面を仮でいれてください。 ・「shop name」 ・「handmade design」 雰囲気については、添付ファイルの「reference」内のデザインをご確認ください。 ・レイアウト、フォント変更OK 文字の大きさについて:特に制限はありませんが、変形文字などはNGとなります。 5.文字の控えについて ・印刷で切れてはいけない重要なデザインは85mm×49mm内に配置してください 6.納品時の注意点 ・aiデータの場合は「アウトライン化済み」「アウトライン化なし」のデータ両方の納品をお願いします ・psdデータの場合はレイヤーは統合せずに分けた状態での納品をお願いします 7.その他、デザイン作成においての注意点はテンプレートを参考にしてください ●重要視する点・経験● ・コンセプト(3.作成デザインについて)にそった的確なデザイン提案をしてくださる方 ・クライアント企業とのコミュニケーションに慣れており、細かい修正依頼にも対応いただける方 ●注意点・禁止事項● ※デザインはオリジナルのもののみとします。 ※ワークリンガの規約により、採用作品の著作権は納品・契約完了後は当社が所有することになります。 ※採用作品の販売・使用・公表の権利は弊社のものとさせて頂き、弊社サイト(カミエル。)上での商用利用に使用させて頂きます。 ※契約が成立した場合でも、盗作等が発覚した場合や他でも同じデザインが使用されている等が発覚した場合は契約を破棄させて頂きます。 では皆様のご応募お待ちしております。 |
採用の理由
シンプルでありながらも おしゃれな雰囲気が社内で人気でしたので、
こちらのデザインを採用とさせていただきます。ステキなご提案をありがとうございました。
応募者全員へのお礼・コメント
皆様、この度のコンペにもたくさんのご提案をありがとうございました。
ハンドメイドカードは弊社初の試みでしたが、ステキなデザインを多数ご提案いただき
サイトオープンが待ち遠しいものとなりました。
また機会がございましたらコンペを行いますので、ご協力をいただけましたら幸いです。

```html
<!DOCTYPE html>
<html lang="en">
<head>
<meta charset="utf-8">
<title>Handmade Tag Card – Shop Name</title>
<link rel="stylesheet" href="https://fonts.googleapis.com/css2?family=Zilla+Slab:wght@400;500&display=swap">
<style>
  :root {
    --paper: #eeecca;
    --paper-soft: #f4f2da;
    --tag-white: #ffffff;
    --wreath-leaf: #b9c79a;
    --wreath-bloom: #e8b7a8;
    --shop-red: #d6434b;
    --ink: #1f1f1f;
  }
  * { margin: 0; padding: 0; box-sizing: border-box; }
  html, body {
    width: 1200px;
    height: 726px;
    overflow: hidden;
    background: var(--paper);
  }
  .sheet {
    position: relative;
    width: 1200px;
    height: 726px;
    background: var(--paper);
  }
  .tag {
    position: absolute;
    top: 0;
    width: 590px;
    height: 726px;
  }
  .tag--left { left: 5px; }
  .tag--right { left: 595px; }
  .tag__art {
    position: absolute;
    left: 0;
    top: 0;
    width: 590px;
    height: 600px;
  }
  .tag__text {
    position: absolute;
    left: 0;
    width: 590px;
    text-align: center;
    font-family: "Zilla Slab", Georgia, serif;
    line-height: 1;
  }
  .shop-name {
    top: 578px;
    font-size: 42px;
    font-weight: 500;
    color: var(--shop-red);
  }
  .shop-tagline {
    top: 634px;
    font-size: 36px;
    font-weight: 400;
    color: var(--ink);
    letter-spacing: 0.5px;
  }
</style>
</head>
<body>
<main class="sheet">
  <section class="tag tag--left">
    <svg class="tag__art" viewBox="0 0 590 600" aria-hidden="false">
      <defs>
        <linearGradient id="wreathToneLeft" x1="0" y1="0" x2="1" y2="1">
          <stop offset="0" stop-color="var(--wreath-bloom)"/>
          <stop offset="0.5" stop-color="var(--wreath-leaf)"/>
          <stop offset="1" stop-color="var(--wreath-bloom)"/>
        </linearGradient>
      </defs>
      <circle class="tag__backdrop" cx="280" cy="322" r="232" fill="var(--paper-soft)"/>
      <circle class="tag__label" cx="300" cy="308" r="228" fill="var(--tag-white)"/>
      <circle class="tag__wreath" role="img" aria-label="Wreath of thin vines with small red, yellow and blue wildflowers"
              cx="292" cy="300" r="250" fill="none" stroke="url(#wreathToneLeft)" stroke-width="34" opacity="0.55"/>
    </svg>
    <p class="tag__text shop-name">shop name</p>
    <p class="tag__text shop-tagline">handmade design</p>
  </section>

  <section class="tag tag--right">
    <svg class="tag__art" viewBox="0 0 590 600" aria-hidden="false">
      <defs>
        <linearGradient id="wreathToneRight" x1="0" y1="0" x2="1" y2="1">
          <stop offset="0" stop-color="var(--wreath-bloom)"/>
          <stop offset="0.5" stop-color="var(--wreath-leaf)"/>
          <stop offset="1" stop-color="var(--wreath-bloom)"/>
        </linearGradient>
      </defs>
      <circle class="tag__backdrop" cx="280" cy="322" r="232" fill="var(--paper-soft)"/>
      <circle class="tag__label" cx="300" cy="308" r="228" fill="var(--tag-white)"/>
      <circle class="tag__wreath" role="img" aria-label="Wreath of thin vines with small red, yellow and blue wildflowers"
              cx="292" cy="300" r="250" fill="none" stroke="url(#wreathToneRight)" stroke-width="34" opacity="0.55"/>
    </svg>
    <p class="tag__text shop-name">shop name</p>
    <p class="tag__text shop-tagline">handmade design</p>
  </section>
</main>
</body>
</html>
```